The most amazing design opportunity you will ever get - Plus we may even through in some shares!

We need a new look and feel for our website, something that will knock the socks off our competitors. Something fresh, functional, dynamic and awesome.

Take a look at the attached brief and see if this is something you can get you head around to come up with something just amazing.

A key to your success is to base your design on the Visual Language (colours Black with Orange on white background, integration of cogs, font, style) and remember that our target audience is BUSINESS and the key thing that we are about is INSIGHTS, so if you can include some subtle design that requires insight to use - Perfect!

```html
<!DOCTYPE html>
<html lang="en">
<head>
<meta charset="utf-8">
<title>Cogwise Insights</title>
<link href="https://fonts.googleapis.com/css2?family=Open+Sans:wght@400;600;700&display=swap" rel="stylesheet">
<style>
:root{
  --orange:#e8842b;
  --orange-dark:#d0701c;
  --black:#111;
  --grey-bar:#6f6f6f;
  --footer:#9b9b9b;
  --text:#444;
  --cream:#fdd08f;
  --page:#fff;
}
*{margin:0;padding:0;box-sizing:border-box}
html,body{width:864px;height:1200px;overflow:hidden}
body{font-family:'Open Sans',sans-serif;color:var(--text);background:var(--page);position:relative;font-size:8px}
.abs{position:absolute}
.stats{left:94px;top:0;width:676px;height:32px;background:var(--grey-bar);border:2px solid var(--orange);border-top:0;display:flex}
.stats .audience{width:66px;background:#f1e6d8;color:var(--orange);font-size:9px;padding:2px 6px;border-right:2px solid var(--orange)}
.stats .audience .crowd{display:block;width:34px;height:10px;margin-top:2px;background:linear-gradient(90deg,#b9a070,#88a06a,#c58a60)}
.stats .cell{flex:1;color:#fff;text-align:center;font-size:7.5px;line-height:11px;padding-top:4px;border-right:1px solid #c98b44}
.stats .cell:last-child{border-right:0}
.stats .cell i{display:block;font-style:italic;font-size:7px}
.logo{left:94px;top:56px;display:flex;align-items:center;gap:8px}
.logo .name{font-size:30px;font-weight:700;color:var(--black);letter-spacing:-1px}
.logo .tag{font-size:8.5px;line-height:11px;color:var(--black)}
.news{left:360px;top:46px;width:392px;height:55px;border:1px solid #ccc;border-radius:3px;background:#f6f6f6}
.news .tabs{display:flex;gap:1px}
.news .tabs span{background:#9a9a9a;color:#fff;font-size:10px;padding:3px 4px}
.news .tabs span.on{background:var(--orange)}
.news p{font-size:7.5px;line-height:14px;padding:2px 10px;color:#333;text-align:justify}
.nav{left:94px;top:118px;width:676px;height:31px;background:var(--black);color:#fff;font-size:9px}
.nav .ins{position:absolute;left:0;top:0;height:31px;width:74px;padding:9px 10px;border-right:1px solid #444}
.nav .about{position:absolute;right:0;top:0;height:31px;width:70px;padding:8px 8px;border-left:1px solid #444;font-size:11px}
h2{color:var(--orange);font-weight:600;font-size:17px}
.why{left:109px;top:170px}
.why-p{left:109px;top:206px;width:660px;font-size:7.5px;line-height:14px;color:#555}
.sec2{left:109px;top:280px}
.slider{left:102px;top:318px;width:660px;height:220px;border:1px solid #bbb}
.slider .art{width:100%;height:100%;background:linear-gradient(90deg,#2f74c8,#d64a9a 35%,#fff 55%,#f2c430 75%,#25a07a)}
.pager{right:6px;bottom:8px;display:flex;gap:2px;align-items:center}
.pager b{background:#333;color:#fff;font-size:10px;width:16px;height:16px;text-align:center;line-height:16px;font-weight:400}
.pager em{font-style:normal;color:#333;margin:0 4px}
.sec3{left:109px;top:568px;font-size:18px}
.card{top:604px;width:316px;height:220px;border:1px solid #aaa}
.card .photo{height:110px}
.card h3{color:var(--orange);font-size:10px;font-weight:600;margin:8px 0 0 30px}
.card ul{list-style:none;position:absolute;top:146px;font-size:7.5px;line-height:14.2px}
.card li:before{content:"";display:inline-block;width:5px;height:5px;border:1.5px solid #222;border-radius:50%;margin-right:5px}
.footer{left:94px;top:856px;width:676px;height:186px;background:var(--footer);color:#222}
.fcol{position:absolute;font-size:7.5px;line-height:14.2px}
.fcol h4{font-size:10px;font-weight:600;line-height:14px;margin-bottom:1px}
.bottom-links{left:96px;top:1060px;font-size:7.5px;display:flex;gap:0}
.bottom-links span{margin-right:31px}
.social{left:102px;top:1101px;display:flex;gap:6px}
.social i{width:22px;height:22px;border-radius:50%;display:block}
.copy{left:102px;top:1150px;font-size:7.5px;line-height:14px}
.video{left:560px;top:1062px;width:202px;height:112px;background:linear-gradient(135deg,#2a6a7a,#6a3a6a,#6a7a2a,#2a2a2a)}
.video .play{position:absolute;left:85px;top:38px;width:32px;height:24px;border-radius:6px;background:#222}
.video .play:after{content:"";position:absolute;left:13px;top:7px;border-left:9px solid #fff;border-top:5px solid transparent;border-bottom:5px solid transparent}
.video span{position:absolute;left:78px;top:94px;color:#fff;font-size:9px}
.x1{left:797px;top:912px;font-size:7px;color:#333}
.shade{left:0;top:0;width:864px;height:1200px;background:rgba(0,0,0,.34)}
.modal{left:192px;top:105px;width:481px;height:394px;background:#fff;border-radius:8px;overflow:hidden}
.modal .close{position:absolute;right:12px;top:13px;width:9px;height:9px;border:1px solid #555;font-size:7px;line-height:7px;text-align:center}
.modal .title{position:absolute;left:97px;top:22px;display:flex;align-items:center;gap:10px;color:var(--orange);font-size:24px}
.modal .title b{color:var(--black);font-size:24px}
.field{position:absolute;left:103px;width:275px;height:22px;border:1px solid #bbb;border-radius:5px;font-size:7.5px;color:#777;padding:5px 9px}
.forgot{position:absolute;left:146px;top:152px;font-size:7.5px;font-style:italic}
.btn{position:absolute;left:143px;width:195px;height:40px;border-radius:7px;font-size:17px;font-weight:700;text-align:center;line-height:40px;box-shadow:2px 3px 3px rgba(0,0,0,.3)}
.btn.login{top:165px;background:var(--orange);color:#fff}
.join{position:absolute;left:0;top:237px;width:481px;height:157px;background:var(--cream);text-align:center}
.join h3{color:var(--orange-dark);font-weight:400;font-size:19px;margin-top:21px}
.join p{font-size:12px;color:#222;margin-top:5px}
.btn.signup{top:95px;background:#fff;color:var(--orange)}
</style>
</head>
<body>
<div class="abs stats">
  <div class="audience">Everyone<span class="crowd" role="img" aria-label="small crowd of people"></span></div>
  <div class="cell"><i>13,458</i>iMembers</div>
  <div class="cell"><i>1,700,250</i>iPoints</div>
  <div class="cell"><i>800,1254</i>iAttributes</div>
  <div class="cell"><i>600,100</i>iActivity</div>
  <div class="cell"><i>300, 150</i>iNetworking</div>
  <div class="cell"><i>i$900,125</i>iDollars</div>
  <div class="cell"><i>900,000</i>iShares</div>
</div>
<div class="abs logo"><span class="name">Cogwise</span><span class="tag">BUSINESS<br>SOLUTIONS<br>THROUGH<br>INSIGHT</span></div>
<div class="abs news">
  <div class="tabs"><span>promotions</span><span>New Affiliates</span><span>Goals</span><span class="on">Did yoiu KNow?</span><span>Hot Tip</span><span>Competition</span></div>
  <p>Lorem ipsum dolor sit amet, consectetur adipisicing elit, sed do eiusmod tempor incididunt ut labore et dolore magna aliqua. Ut enim ad minim veniam... <span style="float:right">more</span></p>
</div>
<div class="abs nav"><div class="ins">Insights</div><div class="about">About Us</div></div>
<h2 class="abs why">Why Cogwise B</h2>
<p class="abs why-p">We are dedicated to helping business people find solutions and insights across 20 business disciplines, your trusted advisor in the global community. Start out today.</p>
<h2 class="abs sec2">21 Business</h2>
<div class="abs slider">
  <div class="art" role="img" aria-label="colourful interlocking cogs"></div>
  <div class="abs pager"><b>1</b><b>2</b><b>3</b><em>......</em><b>20</b><b>21</b><b>22</b><b>&lt;</b><b>&gt;</b></div>
</div>
<h2 class="abs sec3">Cogwise Business Insights</h2>
<div class="abs card" style="left:102px">
  <div class="photo" role="img" aria-label="graduates in caps and gowns" style="background:linear-gradient(90deg,#3a3a3a,#7a6a5a,#2a2a2a)"></div>
  <h3>Target Audience</h3>
  <ul style="left:30px"><li>Graduates</li><li>Solution Providers,</li><li>Job seekers</li><li>Managers</li><li>Executives</li></ul>
  <ul style="left:175px"><li>MBAs</li><li>Authors of business books</li><li>Entrepreneurs</li><li>Specialists</li><li>Employees</li></ul>
</div>
<div class="abs card" style="left:446px">
  <div class="photo" role="img" aria-label="people walking through a glass building" style="background:linear-gradient(180deg,#1c3f7a,#5a78b0,#22345a)"></div>
  <h3>Affiliate Partners</h3>
  <ul style="left:30px"><li>Grad Schools</li><li>University Faculty</li><li>JCompanies</li></ul>
  <ul style="left:175px"><li>Universities</li><li>Ajob Portals</li><li>Recruiters</li></ul>
</div>
<div class="abs footer">
  <div class="fcol" style="left:6px;top:22px"><h4>Disciplines</h4>Business Analytics<br>Career Development<br>Creating Leverage<br>Crowdsourcing<br>Internet Security<br>Leadership&nbsp;&nbsp;&nbsp;Marketing<br>Performance Management<br>Sales<br>Strategy</div>
  <div class="fcol" style="left:127px;top:37px">Business Tools<br>Change Management<br>Creativity &amp; Innovation<br>Entrepreneurship&nbsp;&nbsp;&nbsp;Future Ideas<br>Knowledge, Technology &amp; Culture<br>NLP - Success Coaching<br>Personal Finance &amp; Investments<br>Social Media<br>Systems Thinking</div>
  <div class="fcol" style="left:285px;top:23px"><h4>Library</h4>About / Search<br>Archive<br>Books<br>Getting Started<br>Index&nbsp;&nbsp;Infographics<br>Links<br>Slides<br>Tutorials<br>Upcoming Topics</div>
  <div class="fcol" style="left:409px;top:23px"><h4>Members</h4>About / Search<br>Individuals<br>Teams<br>Insight Affiliates<br>Affiliate Authors<br>Moderators<br>Channel Partners<br>Shareholders</div>
  <div class="fcol" style="left:517px;top:23px"><h4>Insights</h4>Search/Feed<br><br><h4>Rewards</h4>iPoints<br>iRank<br>iStars<br>iDollars<br>iShares</div>
  <div class="fcol" style="left:595px;top:23px"><h4>Hire me</h4>About / Search<br><br><h4>About Us</h4>Vision etc.<br>The Team<br>Contact Us<br>Membership<br>Policy<br>Terms &amp; Conditions</div>
</div>
<div class="abs x1">X1</div>
<div class="abs bottom-links"><span>Getting Started</span><span>Tutorials</span><span>Insight Points</span><span>Index</span><span>Upcoming Topics</span><span>About us</span></div>
<div class="abs social"><i style="background:#8a2a6a"></i><i style="background:#1a8a3a"></i><i style="background:#6a9ad0"></i><i style="background:#d8c818"></i><i style="background:#e07a2a"></i></div>
<div class="abs copy">Cogwise Insights © 2014.<br>All Rights Reserved.</div>
<div class="abs video" role="img" aria-label="colourful patterned video thumbnail"><div class="play"></div><span>Our Video</span></div>

<div class="abs shade"></div>
<div class="abs modal">
  <div class="close">x</div>
  <div class="title">Join the World of <b>Cogwise</b></div>
  <div class="field" style="top:79px">Email Id@example.com</div>
  <div class="field" style="top:113px">Password ****</div>
  <div class="forgot">Forgot password??</div>
  <div class="btn login">LOG IN</div>
  <div class="join">
    <h3>New Member</h3>
    <p>Not Yet A Member ??? <b style="font-weight:600">Join Us Today !!!</b></p>
    <div class="btn signup">SIGN UP</div>
  </div>
</div>
</body>
</html>
```